www.vandrik.com Sales/Order Page ReDesign

We need a new and amazing design for our sales/order page to attract more costumers and new houses for our portal.

Here is the existing page with the current design: https://www.vandrik.com/sales

We are proud owners of www.hyttetun.no and www.vandrik.com and we want more holiday home owners to join our page so that we can rent out their holiday homes and increase the number of houses on our portal.

To get more homeowners we need a sales page that can sell our products the best way possible. Therefore we want you too blow us away with a fresh, modern, easy understandable and stylish new sales/order page.

The only restrictions we give when it comes to design is that it needs to fit the existing design of our portals, the top and footer are set. Beside that we are open for everything as long as it at once give the customers impression that this is a good, professional page were they just have to put out their houses.

When it comes to content I have added two documents who include the content to put in here and some guidelines on how to organize the page. Please be creative and add necessary graphics, symbols, background pictures and what ever necessary to make this page look professional and appealing to new costumers.

Looking forward to what suggestions we are given.
Updates

We just want to inform that we have updated our brief with a much more concrete description of what content to add on the sale page, and who to structure the content on the page. Hope this helps to make suggestions easier. Looking forward to receive some good contributions.

We would just like to make sure that everyone have understood that we are not asking for a new design suggestion to our portal in general. We are only asking for a redesign of our sales/order page you find here www.vandrik.com/sales. We have to day received some designs for our front page and the design it self was good, but that's not what we are asking for this time and don't want you to use time of something we don't need at the moment. We are looking forward too se some good suggestions.

Project Deadline Extended
Reason: Hello. Thanks for all the great contributions we have been given so fare. We haven't been able to respond to all design and are therefore extending the deadline so that we are able to respond to the designs we have been giver and to gov time to make final changes.

Project Deadline Extended
Reason: We are extending the deadline to give designers time to give new suggestion based on our latest feedback today.

Project Deadline Extended
Reason: Extended so we can receive last design changes.

Target Market(s)

This is a presentation page where we present our product agains new home owner who we what to choose listing there property on or site.

Industry/Entity Type

Sales

Requirements
Must have
• A modern design who calms the costumer down and help them in deciding to chose us, and for them to choose us they need to trust and believe in us. Therefore your main task is to create a page that effectively informs about our product, gets the visitors attentions and make them trust us.
Nice to have
• Examples of good competitors and good order pages we like:

http://www.stayplume.com/info/lyp?icid=IL___O_Text___top_nav_link
https://www.nestorly.com/rooms/new
https://www.quince.com/tablo/compare/
http://www.lodgewick.com/host
Should not have
• - Bad design :-). With bad design we mean design that looks like it's made in 2 seconds by a little child.

```html
<!DOCTYPE html>
<html lang="en">
<head>
<meta charset="utf-8">
<title>Vandrik Holiday Rental – List your property</title>
<link rel="stylesheet" href="https://fonts.googleapis.com/css2?family=Arimo:wght@400;700&family=Roboto+Condensed:wght@300;400;700&display=swap">
<style>
:root{
  --blue-bar:#0a84d6;
  --blue:#0a9ae6;
  --blue-deep:#0b7fd0;
  --navy:#1d3a66;
  --accent:#1e90d6;
  --dark:#4a4a4a;
  --green:#a8d548;
  --green-btn:#8fc13a;
  --line:#d8d8d8;
  --white:#fff;
}
*{box-sizing:border-box;margin:0;padding:0}
html,body{width:839px;height:1200px;overflow:hidden}
body{position:relative;font-family:"Arimo",Arial,sans-serif;background:#fff;color:#333}
.abs{position:absolute}

/* header */
.topbar{left:0;top:0;width:839px;height:36px;background:var(--blue-bar)}
.brand{left:108px;top:0;width:222px;height:108px}
.brand-name{left:0;top:22px;width:190px;text-align:center;font-family:"Roboto Condensed",sans-serif;font-size:34px;font-weight:400;color:#1e90d6;letter-spacing:1px}
.brand-sub{left:0;top:60px;width:190px;text-align:right;padding-right:20px;font-size:10px;color:#1e90d6}
.flag{top:10px;width:22px;height:15px;border-radius:2px}
.flag.no{left:466px;background:#d3242f}
.flag.no::after{content:"";position:absolute;left:6px;top:0;width:4px;height:15px;background:#1f3f8f}
.flag.gb{left:492px;background:#1f3f8f}
.signin{left:524px;top:5px;width:104px;height:27px;background:var(--green-btn);border:1px solid #7aa82e;border-radius:3px;color:#2e4a10;font-size:11px;font-weight:700;line-height:25px;padding-left:30px}
.signin::after{content:"";position:absolute;right:10px;top:11px;border:4px solid transparent;border-top-color:#2e4a10}
.list-link{left:635px;top:10px;color:#fff;font-size:12px;font-weight:700}

/* scenic backdrop */
.scenery{left:0;top:36px;width:839px;height:969px;background:
 linear-gradient(180deg,#fff 0%,#fff 12%,#e8f1fa 22%,#b9d5ef 40%,#7ea8d6 58%,#4f7fbf 70%,#2f6cb5 82%,#1f5aa8 100%)}

/* content card */
.card{left:109px;top:120px;width:620px;height:840px;background:#fff}
.title{left:0;top:158px;width:839px;text-align:center;font-size:24px;font-weight:400;color:var(--navy)}
.subtitle{left:0;top:192px;width:839px;text-align:center;font-size:20px;font-weight:400;color:var(--accent)}

.panel{border:1px solid var(--line);background:#fff}
.panel.managed{left:125px;top:244px;width:384px;height:555px}
.panel.self{left:516px;top:244px;width:194px;height:555px}
.panel-title{position:absolute;left:0;width:100%;text-align:center;white-space:nowrap;font-family:"Roboto Condensed",sans-serif;font-weight:700;font-size:17px;color:var(--navy)}
.panel-lede{position:absolute;left:0;width:100%;text-align:center;font-size:9.5px;line-height:18px;color:#333;white-space:nowrap}

.plan{top:338px;width:177px;height:454px;color:#fff;font-size:9.5px}
.plan.premium{left:133px;background:var(--dark)}
.plan.commission{left:318px;background:var(--green);color:#222}
.plan.diy{left:524px;background:var(--blue)}
.price{position:absolute;top:14px;font-family:"Roboto Condensed",sans-serif;font-weight:300;font-size:30px}
.price.fee{left:10px}
.price.rate{right:14px}
.price-label{position:absolute;top:48px;font-size:11px}
.price-label.fee{left:16px}
.price-label.rate{right:14px}
.plan-rows{position:absolute;top:74px;left:0;width:100%;list-style:none;font-size:8.6px}
.plan-rows li{padding:0 7px;display:flex;align-items:center;border-top:1px solid rgba(255,255,255,.55);line-height:13px}
.plan-rows li.r1,.plan-rows li.r2,.plan-rows li.r3{height:33px}
.plan-rows li.r4{height:32px}
.plan-rows li.r5{height:46px;border-bottom:1px solid rgba(255,255,255,.55)}
.includes{position:absolute;top:262px;left:12px;line-height:15.5px}
.partner-badge{display:block;width:66px;height:18px;margin:10px 0 8px;background:#1ea7e6;border-radius:5px}
.upgrades{line-height:12px}
.upgrades span{display:inline-block;width:52px}
.btn{position:absolute;left:12px;top:428px;width:153px;height:20px;background:#fafafa;border:1px solid #bbb;color:#222;font-size:11px;text-align:center;line-height:18px;white-space:nowrap}

.calc-bar{left:125px;top:804px;width:585px;height:33px;background:var(--blue);color:#fff;font-size:8px}
.calc-icon{position:absolute;left:10px;top:6px}
.calc-label{position:absolute;left:45px;top:12px}
.calc-note{position:absolute;right:14px;top:12px}

.help{left:126px;top:862px;width:583px;height:72px;border:1px solid var(--line);background:#fff}
.help-tag{position:absolute;left:-1px;top:-1px;width:150px;height:72px;background:var(--blue)}
.help-tag::after{content:"";position:absolute;right:-12px;top:24px;border:12px solid transparent;border-left-color:var(--blue);border-right:0}
.help-title{position:absolute;left:20px;top:8px;font-family:"Roboto Condensed",sans-serif;font-size:26px;color:#fff;white-space:nowrap}
.help-sub{position:absolute;left:22px;top:44px;font-family:"Roboto Condensed",sans-serif;font-weight:700;font-size:15px;color:var(--navy)}
.call{position:absolute;left:195px;top:8px;font-size:18px;color:#222;white-space:nowrap}
.call b{font-weight:400;color:var(--accent);font-size:22px;margin-left:6px}
.hours{position:absolute;left:196px;top:36px;font-size:9px;color:#222}
.mail{position:absolute;left:196px;top:56px;font-size:9px;color:#222}
.mail a{color:var(--accent);text-decoration:none}
.support-photo{position:absolute;right:0;top:0;width:132px;height:70px;background:linear-gradient(90deg,#fff 0%,#e9eef3 40%,#d6c3b3 100%)}

/* footer */
.footer{left:0;top:1005px;width:839px;height:195px;background:var(--blue-deep);color:#fff;font-size:9px}
.fcol{position:absolute;top:36px}
.fcol h4{font-size:10.5px;font-weight:700;margin-bottom:6px}
.fcol ul{list-style:none}
.fcol li{height:13.5px;padding-left:18px;position:relative;white-space:nowrap}
.arrow li::before{content:"";position:absolute;left:2px;top:1px;width:9px;height:9px;border-radius:50%;background:#fff}
.arrow li::after{content:"";position:absolute;left:6px;top:3.5px;border:2px solid transparent;border-left:3px solid var(--blue-deep)}
.divider{position:absolute;top:0;width:1px;height:140px;background:rgba(255,255,255,.18)}
.world-map{position:absolute;left:198px;top:32px;width:110px;height:64px;background:radial-gradient(ellipse at center,rgba(255,255,255,.85) 0%,rgba(255,255,255,.55) 55%,rgba(255,255,255,0) 72%)}
.contact li{padding-left:24px}
.contact svg{position:absolute;left:2px;top:0}
</style>
</head>
<body>

<div class="abs topbar"></div>
<div class="abs scenery" role="img" aria-label="Scenic Norwegian fjord with mountains, sea and a fishing village"></div>

<header>
  <div class="abs brand">
    <svg class="abs" width="222" height="108" viewBox="0 0 222 108" aria-hidden="true">
      <path d="M0 0H222V94L111 70L0 94Z" fill="#f4f4f4"/>
      <path d="M0 94L111 70L222 94V108L111 84L0 108Z" fill="#444"/>
    </svg>
    <div class="abs brand-name">VANDRIK</div>
    <div class="abs brand-sub">HOLIDAY RENTAL</div>
  </div>
  <div class="abs flag no" aria-label="Norsk"></div>
  <div class="abs flag gb" aria-label="English"></div>
  <div class="abs signin">Sign in</div>
  <div class="abs list-link">List your property</div>
</header>

<main>
  <div class="abs card"></div>
  <h1 class="abs title">How do you want to list your property?</h1>
  <h2 class="abs subtitle">Please choose a Listing Option.</h2>

  <section class="abs panel managed">
    <h3 class="panel-title" style="top:16px">Save time while we create income on your property</h3>
    <p class="panel-lede" style="top:42px">Let our professional team handle your inquiries and bookings, and just sit and wait for<br>the costumer to arrive at your property knowing you will get paid.</p>
  </section>
  <section class="abs panel self">
    <h3 class="panel-title" style="top:20px;font-size:19px">Do it yourself</h3>
    <p class="panel-lede" style="top:46px">Handle inquiries and bookings yourself,<br>with help with our advance tools</p>
  </section>

  <div class="abs plan premium">
    <div class="price fee">€ 995</div><div class="price rate">0%</div>
    <div class="price-label fee">Annually</div><div class="price-label rate">per booking</div>
    <ul class="plan-rows">
      <li class="r1">Our professional team is there for you</li>
      <li class="r2">One upfront fee</li>
      <li class="r3">No limits or fee on bookings.</li>
      <li class="r4">No limits or fee on bookings request</li>
      <li class="r5">Advertise your property for 12 months</li>
    </ul>
    <div class="includes">Include announcements on:<br>Hyttetun.no<br>Vandrik.com<br>Torgly.no
      <span class="partner-badge" aria-label="Torgly.no listing badge"></span>
      <div class="upgrades">Upgrade with Torgly.no:<br>
        <span>&nbsp;60 days</span>€ &nbsp;50<br>
        <span>&nbsp;120 days</span>€ &nbsp;90<br>
        <span>&nbsp;240 days</span>€ 160<br>
        <span>&nbsp;1 year</span>€ 240</div>
    </div>
    <div class="btn">Start Building Your Listing</div>
  </div>

  <div class="abs plan commission">
    <div class="price fee">€ 0</div><div class="price rate">18%</div>
    <div class="price-label fee">Annually</div><div class="price-label rate">per booking</div>
    <ul class="plan-rows">
      <li class="r1">Our professional team is there for you</li>
      <li class="r2">No listing fee</li>
      <li class="r3">No limits on bookings.</li>
      <li class="r4">No limits or fee on bookings request</li>
      <li class="r5">You decide when to advertise and for how long</li>
    </ul>
    <div class="includes">Include announcements on:<br>Hyttetun.no<br>Vandrik.com</div>
    <div class="btn">Start Building Your Listing</div>
  </div>

  <div class="abs plan diy">
    <div class="price fee">€ 0</div><div class="price rate">2%</div>
    <div class="price-label fee">Annually</div><div class="price-label rate">per booking</div>
    <ul class="plan-rows">
      <li class="r1">You handle everything yourself</li>
      <li class="r2">No listing fee</li>
      <li class="r3">No limits on bookings.</li>
      <li class="r4">No limits or fee on bookings request</li>
      <li class="r5">You decide when to advertise and for how long</li>
    </ul>
    <div class="includes">Include announcements on:<br>Hyttetun.no<br>Vandrik.com</div>
    <div class="btn">Start Building Your Listing</div>
  </div>

  <div class="abs calc-bar">
    <svg class="calc-icon" width="18" height="22" viewBox="0 0 18 22" aria-hidden="true">
      <rect x="1" y="1" width="16" height="20" rx="2" fill="none" stroke="#fff" stroke-width="1.5"/>
      <rect x="4" y="4" width="10" height="4" fill="#fff"/>
      <g fill="#fff"><rect x="4" y="10" width="2.5" height="2.5"/><rect x="7.75" y="10" width="2.5" height="2.5"/><rect x="11.5" y="10" width="2.5" height="2.5"/><rect x="4" y="14" width="2.5" height="2.5"/><rect x="7.75" y="14" width="2.5" height="2.5"/><rect x="11.5" y="14" width="2.5" height="2.5"/></g>
    </svg>
    <span class="calc-label">Booking Comparison Calculator</span>
    <span class="calc-note">* Transaction fee for secure payment 4.5% comes in addition</span>
  </div>

  <section class="abs help">
    <div class="help-tag">
      <div class="help-title">Need Help?</div>
      <div class="help-sub">CONTACT US</div>
    </div>
    <div class="call">Call us: <b>+47 21 48 30 75</b></div>
    <div class="hours">M-F 8am-7pm, Sat 8am-4pm</div>
    <div class="mail">Email: <a>propertymanagers@vandrik.com</a></div>
    <div class="support-photo" role="img" aria-label="Customer support staff wearing headsets"></div>
  </section>
</main>

<footer class="abs footer">
  <div class="fcol arrow" style="left:120px">
    <h4>Destinations</h4>
    <ul><li>Europe</li><li>North America</li><li>South America</li><li>Africa</li><li>Asia</li><li>Australia</li></ul>
  </div>
  <div class="world-map" role="img" aria-label="World map"></div>
  <div class="divider" style="left:355px"></div>
  <div class="fcol arrow" style="left:367px">
    <h4>For tenants</h4>
    <ul><li>My page</li><li>Why Vandrik?</li><li>Help</li><li>Rental terms</li></ul>
  </div>
  <div class="divider" style="left:465px"></div>
  <div class="fcol arrow" style="left:477px">
    <h4>For house owners</h4>
    <ul><li>MyAdmin</li><li>Let us rent your house</li><li>Conditions</li></ul>
  </div>
  <div class="divider" style="left:605px"></div>
  <div class="fcol contact" style="left:619px;top:28px">
    <h4>Contact us</h4>
    <ul>
      <li>Vandrik Holiday Rental</li>
      <li><svg width="10" height="8" viewBox="0 0 10 8" aria-hidden="true"><rect x=".5" y=".5" width="9" height="7" fill="none" stroke="#fff"/><path d="M.5 .5L5 4.5L9.5 .5" fill="none" stroke="#fff"/></svg>post@vandrik.com</li>
      <li><svg width="10" height="10" viewBox="0 0 10 10" aria-hidden="true"><path d="M2 1l2 2-1 1.5c.8 1.5 1.5 2.2 3 3L7.5 6.5l2 2L8 10C4 9.5.5 6 0 2Z" fill="#fff"/></svg>+47 21 48 30 75</li>
      <li><svg width="10" height="10" viewBox="0 0 10 10" aria-hidden="true"><circle cx="5" cy="5" r="4.3" fill="none" stroke="#fff"/><ellipse cx="5" cy="5" rx="2" ry="4.3" fill="none" stroke="#fff"/><path d="M.7 5h8.6" stroke="#fff"/></svg>www.vandrik.com</li>
    </ul>
    <h4 style="margin-top:4px">Opening hours</h4>
    <ul>
      <li><svg width="10" height="10" viewBox="0 0 10 10" aria-hidden="true"><circle cx="5" cy="5" r="4.3" fill="none" stroke="#fff"/><path d="M5 2.5V5h2" fill="none" stroke="#fff"/></svg>Mon - Fri: 9.00 AM - 5.00 PM</li>
      <li><svg width="10" height="10" viewBox="0 0 10 10" aria-hidden="true"><circle cx="5" cy="5" r="4.3" fill="none" stroke="#fff"/><path d="M5 2.5V5h2" fill="none" stroke="#fff"/></svg>Sat - Sun: Closed</li>
    </ul>
  </div>
</footer>

</body>
</html>
```